A5 Flyer for mobile App development

We need a double sided flyer design that will need to be printed on A5 sized paper.
The design will be based on a phone/tablet look and feel.

The idea behind the pamphlet is that we show clients that they can have a mobile app white labelled to their company/brand.

The front of the pamphlet will need to look like a front of a phone with a generic mobile app running within the phone.
The phone must not resemble a real phone, however, it should resemble a cartoon look phone - similar to the attached image called "phone.jpg". The mobile app running within the phone needs to have a "drawing/wireframe" look - similar to the "mock.jpg" image attached. The logo part should look like a "placeholder" image - similar to the image named "mocklogo" (look at the far left) attached.

The back of the pamphlet must also be similar, so that when you turn over the pamphlet, it should look like you're turning over a real phone, and you're now the seeing the back of the phone.
The back of the phone should be styled similar to the front. The text and items on the back of the phone are also in the image named "20170503_212415.jpg".

The phone on the pamphlet should not have an outline, meaning that the pamphlet will have rounded corners, giving the phone a shape.

Please send us a message if you're unsure about anything.

Target Market(s)

Businesses that have salons, spa's, beauty clinics, etc.

Industry/Entity Type

Health And Wellness

Font styles to use
Sans Serif
Script

Colors
e34297

Requirements
Must have
• The pamphlet will have rounded corners, giving the phone its look. See attached the image named "brennolux.."
Should not have
• the phone on the pamphlet should not have an outline, meaning that the pamphlet will have rounded corners, giving the phone a shape. Please have a look at the brennolux image attached that demonstrates the cut out lines.

```html
<!DOCTYPE html>
<html lang="en">
<head>
<meta charset="utf-8">
<title>A5 App Flyer – Front and Back</title>
<link rel="stylesheet" href="https://fonts.googleapis.com/css2?family=Montserrat:wght@400;600;700;800&family=Dosis:wght@500;600&display=swap">
<style>
  :root{
    --canvas:#ffffff;
    --shell-dark:#8f9294;
    --shell-mid:#b7b9ba;
    --shell-light:#d9dadb;
    --bezel:#7c7f81;
    --screen-pink:#b0297a;
    --screen-deep:#8a1b5e;
    --screen-soft:#c86aa2;
    --title-pink:#f6dbea;
    --cta-green:#4cb85a;
    --brand-red:#c4000b;
    --band-grey:#acadae;
    --text-grey:#8f9092;
    --price-grey:#6f7072;
    --white:#ffffff;
  }
  html,body{margin:0;padding:0;overflow:hidden;background:var(--canvas);}
  .canvas{position:relative;width:1200px;height:878px;overflow:hidden;background:var(--canvas);font-family:"Montserrat",Arial,sans-serif;}

  /* ---------- front of phone ---------- */
  .phone-front{position:absolute;left:78px;top:80px;width:492px;height:696px;border-radius:30px;
    background:linear-gradient(135deg,var(--shell-mid) 0%,var(--shell-light) 35%,var(--shell-dark) 70%,var(--shell-light) 100%);}
  .phone-front .bezel{position:absolute;left:14px;top:14px;right:14px;bottom:14px;border-radius:22px;
    border:5px solid var(--bezel);box-sizing:border-box;
    background:linear-gradient(135deg,#c9cacb 0%,#e4e5e6 40%,#a5a7a8 75%,#cfd0d1 100%);}
  .speaker{position:absolute;left:195px;top:27px;width:78px;height:8px;border-radius:4px;background:#6e7173;}
  .screen{position:absolute;left:19px;top:47px;width:420px;height:540px;overflow:hidden;
    background:linear-gradient(160deg,var(--screen-soft) 0%,var(--screen-pink) 45%,var(--screen-deep) 100%);}
  .screen .sheen{position:absolute;inset:0;}
  .logo-placeholder{position:absolute;left:146px;top:52px;width:124px;height:124px;}
  .brand-title{position:absolute;left:0;right:0;top:190px;margin:0;text-align:center;color:var(--title-pink);
    font-weight:700;font-size:70px;line-height:57px;letter-spacing:-3px;}
  .cta{position:absolute;left:74px;top:408px;width:264px;height:36px;background:var(--cta-green);color:var(--white);
    font-weight:700;font-size:26px;letter-spacing:9px;line-height:36px;text-align:center;}
  .home-button{position:absolute;left:206px;top:596px;width:46px;height:46px;}

  /* ---------- back of phone ---------- */
  .phone-back{position:absolute;left:624px;top:80px;width:490px;height:696px;border-radius:30px;overflow:hidden;
    background:linear-gradient(180deg,var(--shell-light) 0%,#cfd0d1 100%);}
  .phone-back .rim{position:absolute;left:14px;top:14px;right:14px;bottom:14px;border-radius:22px;border:4px solid #ebebeb;box-sizing:border-box;}
  .camera{position:absolute;left:190px;top:42px;width:110px;height:52px;border-radius:26px;
    border:3px solid #e6e6e6;box-sizing:border-box;background:#c6c7c8;}
  .camera .lens{position:absolute;top:12px;width:28px;height:28px;border-radius:50%;}
  .camera .lens.dark{left:15px;background:#8e9092;}
  .camera .lens.light{left:61px;background:#eeeeee;}
  .brand-name{position:absolute;left:0;right:0;top:140px;text-align:center;
    color:var(--brand-red);font-weight:700;font-size:40px;line-height:50px;letter-spacing:1px;}
  .brand-name .dot{display:inline-block;width:16px;height:16px;background:var(--brand-red);margin-right:12px;vertical-align:4px;}
  .info-band{position:absolute;left:0;right:0;top:214px;height:328px;
    background:linear-gradient(90deg,#a3a4a5 0%,var(--band-grey) 50%,#b6b7b8 100%);}
  .price{position:absolute;left:0;right:0;top:6px;text-align:center;font-family:"Dosis",Arial,sans-serif;color:var(--price-grey);font-weight:600;}
  .price .from{font-size:38px;}
  .price .amount{font-size:52px;}
  .price .per{font-size:24px;}
  .pitch{position:absolute;left:0;right:0;top:84px;margin:0;text-align:center;color:var(--text-grey);
    font-weight:700;font-size:34px;line-height:37px;letter-spacing:-1.5px;}
  .platforms{position:absolute;left:0;right:0;top:578px;text-align:center;color:#8a8b8d;font-weight:700;font-size:15px;letter-spacing:1px;}
  .platforms .mark{display:inline-block;width:10px;height:10px;background:#8a8b8d;margin-right:6px;vertical-align:0;}
  .web{position:absolute;left:0;right:0;top:624px;text-align:center;color:#9a9b9d;font-weight:600;font-size:19px;letter-spacing:2px;}
</style>
</head>
<body>
<div class="canvas">

  <section class="phone-front" aria-label="Flyer front">
    <div class="bezel">
      <div class="speaker"></div>
      <div class="screen" role="img" aria-label="Pink app screen with a faint wireframe grid pattern">
        <svg class="sheen" width="420" height="540" viewBox="0 0 420 540">
          <polygon points="0,0 212,0 340,540 0,540" fill="#ffffff" opacity="0.16"/>
        </svg>
        <svg class="logo-placeholder" viewBox="0 0 124 124" aria-label="Logo placeholder">
          <circle cx="62" cy="62" r="62" fill="#f2d6e7" opacity="0.85"/>
          <circle cx="48" cy="42" r="9" fill="#c45a96"/>
          <polygon points="30,86 54,54 66,70 74,58 96,86" fill="#c45a96"/>
        </svg>
        <h1 class="brand-title">YOUR<br>BRAND<br>HERE</h1>
        <div class="cta">BOOK NOW</div>
      </div>
      <svg class="home-button" viewBox="0 0 50 50" aria-hidden="true">
        <path d="M8 34 A22 22 0 1 1 34 44" fill="none" stroke="#6e7173" stroke-width="2"/>
      </svg>
    </div>
  </section>

  <section class="phone-back" aria-label="Flyer back">
    <div class="rim"></div>
    <div class="camera"><span class="lens dark"></span><span class="lens light"></span></div>
    <div class="brand-name"><span class="dot"></span>GLOWBOOK</div>
    <div class="info-band">
      <div class="price"><span class="from">from </span><span class="amount">R499</span><span class="per">pm</span></div>
      <p class="pitch">LET YOUR<br>CLIENTS BOOK<br>THEIR NEXT<br>APPOINTMENT<br>USING<br>YOUR APP</p>
    </div>
    <div class="platforms"><span class="mark"></span>OS ONE &nbsp; OS TWO</div>
    <div class="web">email:www.slotbook-demo.com</div>
  </section>

</div>
</body>
</html>
```